Minimalist Professional Business Card Design

We will be revamping our marketing materials: Business cards, Website and Catalogs.
Our Overall Design direction is to have a Minimalist artwork with Professionalism and Premium feel. The revamp starts with the new business card design followed by the others. Thus the designer whom work is selected for this job will likely to follow through with the subsequent jobs.

Target Market(s)

Upscale

Industry/Entity Type

Manufacturing

Contact Information for Business Card

For the Business Cards, the following are required:
. Minimalist yet Professional and Premium Feel
. Background Colors: white and / or light pastel yellow and if needed to smoothen the yellow, the light grey can be incorporated. We are changing our corporate bright yellow to either one of the three alternatives:
1. Soylant yellow CMYK (1%, 0%, 52%, 3%)
2. Popcorn yellow CMYK (0%, 0%, 33%, 0%)
3. Papaya yellow CMYK (0%, 0%, 51%, 0%)

Information to be inputed in the business cards:

Name: Barlen Moritova
Position: Managing Director

Company's name: Vellomar Valves Pte. Ltd.
Address: 512 Halvick Lane #07-09B
Singapore 617302
Tel: (65) 6281 4096
Fax: (65) 6294 7118
Email: barlen@vellomarvalves-example.com
Website: www.vellomarvalves-example.com
Skype: Vellomar.Valves
Whatsapp/ Line/ Viber/ WeChat: (65) 9372 6081

Company's Logo
Company's Slogan
Two product photos placed side by side (if this gets into the way of the design, it is OK not to include them)

Font styles to use
Serif

Colors
ffffff

Requirements
Must have
• Minimalist
Should not have
• Messy, crowded, playful

```html
<!DOCTYPE html>
<html lang="en">
<head>
<meta charset="utf-8">
<title>Vellomar Valves – Business Card</title>
<link rel="stylesheet" href="https://fonts.googleapis.com/css2?family=Jost:wght@400;500;600;700&display=swap">
<style>
  :root {
    --slate: #5a5b5b;
    --pastel-yellow: #fff59a;
    --backdrop: #ebe8e1;
    --white: #ffffff;
    --shadow: 0 10px 18px rgba(0,0,0,0.18);
  }
  * { box-sizing: border-box; margin: 0; padding: 0; }
  html, body {
    width: 1200px; height: 1200px; overflow: hidden;
    background: var(--backdrop);
    font-family: "Jost", sans-serif;
  }
  .card {
    position: absolute; left: 265px; width: 670px; height: 382px;
    background: var(--pastel-yellow); box-shadow: var(--shadow);
    overflow: hidden;
  }
  .card-front { top: 172px; }
  .card-back { top: 645px; }

  .brand-panel {
    position: absolute; left: 0; top: 0; width: 282px; height: 100%;
    background: var(--slate);
    display: flex; flex-direction: column; align-items: center; justify-content: center;
    gap: 14px; padding-bottom: 20px;
  }
  .brand-mark {
    width: 104px; height: 104px; border-radius: 50%;
    border: 9px solid currentColor;
  }
  .brand-panel .brand-mark { color: var(--white); }
  .brand-name {
    font-weight: 600; letter-spacing: 1px; line-height: 1;
  }
  .brand-panel .brand-name { color: var(--white); font-size: 38px; }

  .name-band {
    position: absolute; left: 336px; top: 66px; width: 334px; height: 72px;
    background: var(--slate); color: var(--white);
    text-align: right; padding: 7px 14px 0 0;
  }
  .person-name { font-size: 30px; font-weight: 600; letter-spacing: 0.8px; line-height: 1.1; }
  .person-title { font-size: 17.5px; font-weight: 400; letter-spacing: 0.6px; margin-top: 1px; }

  .contact-list {
    position: absolute; left: 315px; top: 176px;
    color: var(--slate); font-size: 13px; font-weight: 500;
    letter-spacing: 0.4px; line-height: 16.8px; text-transform: uppercase;
    list-style: none;
  }
  .contact-list .group-gap { margin-top: 16px; }

  .back-lockup {
    position: absolute; inset: 0;
    display: flex; flex-direction: column; align-items: center; justify-content: center;
    color: var(--slate); padding-bottom: 6px;
  }
  .back-lockup .brand-mark { width: 110px; height: 110px; }
  .back-lockup .brand-name { font-size: 46px; margin-top: 12px; }
  .company-name { font-size: 25px; font-weight: 700; letter-spacing: 1px; margin-top: 8px; line-height: 1.1; }
  .slogan { font-size: 15px; font-weight: 500; letter-spacing: 0.6px; text-transform: uppercase; }
</style>
</head>
<body>
  <section class="card card-front">
    <div class="brand-panel">
      <div class="brand-mark"></div>
      <div class="brand-name">VELLOMAR</div>
    </div>
    <div class="name-band">
      <div class="person-name">BARLEN MORITOVA</div>
      <div class="person-title">MANAGING DIRECTOR</div>
    </div>
    <ul class="contact-list">
      <li>Address: 512 Halvick Lane #07-09B</li>
      <li>Singapore 617302</li>
      <li class="group-gap">Tel: (65) 6281 4096</li>
      <li>Fax: (65) 6294 7118</li>
      <li class="group-gap">Email: barlen@vellomarvalves-example.com</li>
      <li>Website: www.vellomarvalves-example.com</li>
      <li>Skype: Vellomar.Valves</li>
      <li>Whatsapp/ Line/ Viber/ WeChat: (65) 9372 6081</li>
    </ul>
  </section>

  <section class="card card-back">
    <div class="back-lockup">
      <div class="brand-mark"></div>
      <div class="brand-name">VELLOMAR</div>
      <div class="company-name">VELLOMAR VALVES PTE. LTD.</div>
      <div class="slogan">Built with care I for hard work</div>
    </div>
  </section>
</body>
</html>
```